Design a fun and engaging Social Media eBook

Graphic design job:

For initial concept stage, please provide some sample powerpoint designs of:
-A cover
-Section divides
-A few copy pages

We can then work on the full document which would be redesigning 22 pages of existing copy in word docs into the template.

Will be used to educate staff on Social Media.
We would like the design of the document to reflect the digital and social landscape. It should be fun and engaing.

Should demonstrate creativity, have social community focus, and be colourful and modern.

The audience is older people that need to be convinced about the benefits of social media and require some education / tips on how to use it. 40-60 year olds.

To be supplied to us in powerpoint.

Reason: This project has been extended, we have changed the category to graphic design and simplified the initial concept phase for designers to submit ideas.

Target Market(s)

Older staff that need to get the benefits of social media

Industry/Entity Type

Education

Requirements
Must have
• Must be supplied in Powerpoint.
Look modern, slick, cool, edgy

Look very "Tindro" brand in simplicity and digital sense.
Reflect a 'digital' type of design

Combine all documents into one clean document / workbook.

(Don't worry will not be ised for powerpoint presentations, just want it in an edible document format - so lots of text on a slide is fine) Finished product will be a PDF
Nice to have
• Interactive in some way with click throughs or page turners

```html
<!DOCTYPE html>
<html lang="en">
<head>
<meta charset="utf-8">
<title>Creating Content – What kind of content should I post?</title>
<link rel="stylesheet" href="https://fonts.googleapis.com/css2?family=Nunito+Sans:wght@400;600&display=swap">
<style>
  :root {
    --page-bg: #e6e7eb;
    --panel-edge: #c9cacd;
    --accent: #ffa200;
    --accent-soft: #ffe3a8;
    --ink: #4f4f4f;
    --ink-dark: #222222;
    --ink-muted: #5a5a5a;
    --rule: #9b9b9b;
    --nav-bg: #ffffff;
    --button-bottom: #0c0c0c;
    --button-icon: #ffb400;
  }
  * { margin: 0; padding: 0; box-sizing: border-box; }
  html, body { width: 1200px; height: 901px; overflow: hidden; }
  body {
    background: var(--page-bg);
    font-family: "Nunito Sans", Arial, sans-serif;
    color: var(--ink);
    position: relative;
  }
  .page-panel {
    position: absolute;
    left: 21px; top: 22px;
    width: 1161px; height: 792px;
    border: 1px solid var(--panel-edge);
    border-radius: 10px;
    background:
      radial-gradient(ellipse 70% 60% at 70% 45%, #ffffff 0%, rgba(255,255,255,0) 70%),
      linear-gradient(160deg, #f2f2f2 0%, #fbfbfb 45%, #ececec 100%);
    box-shadow: 0 1px 3px rgba(0,0,0,0.12);
    overflow: hidden;
  }
  .section-bar {
    position: absolute;
    left: 0; top: 25px;
    width: 100%; height: 40px;
    background: var(--accent);
    display: flex; align-items: center;
    padding-left: 15px;
    font-size: 24px;
    color: #ffffff;
  }
  .section-number { color: var(--accent-soft); margin-right: 17px; }
  .topic-icon {
    position: absolute;
    left: 32px; top: 90px;
    width: 58px; height: 65px;
    border-radius: 6px;
    background: linear-gradient(135deg, #ffffff 0%, #eef0ee 60%, #cfd9c4 100%);
    box-shadow: 0 1px 3px rgba(0,0,0,0.2);
  }
  .topic-heading {
    position: absolute;
    left: 107px; top: 106px;
    font-size: 22px;
    font-weight: 400;
    color: var(--ink-dark);
  }
  .topic-rule {
    position: absolute;
    left: 111px; top: 139px;
    width: 989px; height: 1px;
    background: var(--rule);
  }
  .body-copy {
    position: absolute;
    left: 168px; top: 0;
    font-size: 19px;
    color: var(--ink);
  }
  .body-copy .line {
    position: absolute;
    left: 0;
    white-space: nowrap;
    line-height: 1;
  }
  .body-copy .bullet { padding-left: 40px; }
  .body-copy .bullet::before {
    content: "";
    position: absolute;
    left: 5px; top: 7px;
    width: 6px; height: 6px;
    border-radius: 50%;
    background: var(--ink);
  }
  .chapter-nav {
    position: absolute;
    left: 15px; top: 687px;
    width: 1134px; height: 94px;
    background: var(--nav-bg);
    border: 1px solid #d4d4d4;
    border-radius: 10px;
    font-size: 14px;
    color: var(--ink-muted);
  }
  .chapter-nav a {
    position: absolute;
    color: inherit;
    text-decoration: none;
    white-space: nowrap;
    line-height: 1;
  }
  .chapter-nav a.is-current { color: var(--accent); }
  .footer-home { position: absolute; left: 62px; top: 826px; }
  .footer-title {
    position: absolute;
    left: 147px; top: 837px;
    font-size: 14.5px;
    color: var(--ink-muted);
  }
  .pager-button {
    position: absolute;
    top: 827px;
    width: 109px; height: 38px;
    border-radius: 5px;
    background: linear-gradient(#3a3a3a, var(--button-bottom));
    box-shadow: 0 1px 2px rgba(0,0,0,0.4);
    color: #ffffff;
    font-size: 15px;
    text-decoration: none;
    display: flex; align-items: center;
  }
  .pager-button.previous { left: 913px; padding-left: 10px; gap: 8px; }
  .pager-button.next { left: 1043px; padding-left: 26px; gap: 13px; }
</style>
</head>
<body>
  <main class="page-panel">
    <header class="section-bar">
      <span class="section-number">02</span>
      <span class="section-title">Creating Content</span>
    </header>

    <div class="topic-icon" role="img" aria-label="Notepad with pencil illustration"></div>
    <h1 class="topic-heading">What kind of content should I post?</h1>
    <div class="topic-rule"></div>

    <div class="body-copy">
      <span class="line" style="top:188px">once your social media pages are all set up and ready to go,&nbsp; what do you post?</span>
      <span class="line" style="top:228px">Take a step back and think about the purpose of social media.&nbsp; What makes it so appealing?</span>
      <span class="line" style="top:309px">It gives people a platform to:</span>
      <span class="line bullet" style="top:350px">connect with other people and network</span>
      <span class="line bullet" style="top:390px">share information and create influence</span>
      <span class="line bullet" style="top:430px">learn and discuss new ideas</span>
      <span class="line bullet" style="top:471px">inspire and be inspired</span>
      <span class="line" style="top:511px">Your social commentary content needs to address these needs.&nbsp; They’re all things that you natu-</span>
      <span class="line" style="top:552px">rally do every day as part of running a successful practice. So see your social media content as</span>
      <span class="line" style="top:592px">simply another means to help you be even more successful.</span>
    </div>

    <nav class="chapter-nav">
      <a href="#" style="left:70px;top:18px">Introduction</a>
      <a href="#" class="is-current" style="left:237px;top:18px">Creating Content</a>
      <a href="#" style="left:419px;top:18px">Social Media Overview</a>
      <a href="#" style="left:631px;top:18px">Tips and pull-out quotes</a>
      <a href="#" style="left:871px;top:18px">Quick Social Media Questionnaire</a>
      <a href="#" style="left:173px;top:54px">Creating Your Company Circlebook Page</a>
      <a href="#" style="left:503px;top:56px">Create a Linkwork Personal Profile</a>
      <a href="#" style="left:783px;top:56px">Social Media Etiquette</a>
    </nav>
  </main>

  <svg class="footer-home" width="38" height="34" viewBox="0 0 38 34" aria-label="Home">
    <path d="M19 2 L2 17 L6 17 L6 32 L15 32 L15 22 L23 22 L23 32 L32 32 L32 17 L36 17 Z" fill="#6b6b6b"/>
  </svg>
  <span class="footer-title">Harbourline Wealth Advisory</span>

  <a class="pager-button previous" href="#">
    <svg width="20" height="20" viewBox="0 0 20 20" aria-hidden="true">
      <rect x="0" y="0" width="20" height="20" rx="3" fill="var(--button-icon)"/>
      <path d="M13 5 L6 10 L13 15 Z" fill="#1a1a1a"/>
    </svg>
    <span>Previous</span>
  </a>
  <a class="pager-button next" href="#">
    <span>Next</span>
    <svg width="20" height="20" viewBox="0 0 20 20" aria-hidden="true">
      <rect x="0" y="0" width="20" height="20" rx="3" fill="var(--button-icon)"/>
      <path d="M7 5 L14 10 L7 15 Z" fill="#1a1a1a"/>
    </svg>
  </a>
</body>
</html>
```